Mushroom packaging box design

We need for good design for double corrugated box, all the details info and Chinese translation will be provided when the design selected.
.
Task :1
Both of side A needs to put with company info( logo, name , contact details,slogan ,two-dimension code )
Name: Fujian Silverbrook Agronomic Sciences Co.,Ltd.
Address: South of 317 Provincial Road, East of Taoxi Township, City of Longyan, Fujian Province, China.
Head office Tel :
Official website: www.fjqlnykx.com
The Slogan is: we grow healthier future for you.
The two-dimension code should be put in the right corner in both of side A. (we will update in next 5 days)
Both of side B needs to put some three packing marking of handing of goods icons which you can find sample in attachments and also we need put info as below under the three icons.
(product name):
(dimension):
(weight ):
(volume): 65x45x56cm
Overall, project should be simple, organic.

```html
<!DOCTYPE html>
<html lang="en">
<head>
<meta charset="utf-8">
<title>Mushroom Packaging Box Dieline</title>
<link rel="stylesheet" href="https://fonts.googleapis.com/css2?family=Roboto:wght@400;500;700&family=Noto+Sans+SC:wght@700&family=Tinos&display=swap">
<style>
  :root {
    --page: #ffffff;
    --sheet: #ffffff;
    --cut-line: #c9c9c9;
    --fold-line: #d6d6d6;
    --ink: #1e1e1e;
    --logo-frame: #b5b5b5;
    --mark: #1a9e88;
  }
  * { box-sizing: border-box; margin: 0; padding: 0; }
  html, body { width: 1200px; height: 960px; overflow: hidden; background: var(--page); }
  .canvas { position: relative; width: 1200px; height: 960px; }

  .dieline { position: absolute; left: 0; top: 0; }

  .panel { position: absolute; top: 334px; height: 294px; }
  .panel-side-a { width: 298px; }
  .panel-side-b { width: 240px; }

  .logo-slot {
    position: absolute; left: 91px; top: 24px; width: 119px; height: 56px;
    border: 1px solid var(--logo-frame);
    font-family: "Tinos", serif; font-size: 11px; color: #444;
    text-align: center; padding-top: 1px;
  }
  .slogan {
    position: absolute; left: 46px; top: 98px;
    font-family: "Roboto", sans-serif; font-weight: 500; font-size: 13.5px; color: var(--ink);
    white-space: nowrap;
  }
  .company-name, .head-office, .address {
    position: absolute; font-family: "Roboto", sans-serif; font-size: 6.6px;
    line-height: 8.6px; color: var(--ink); font-weight: 500; text-transform: uppercase;
  }
  .company-name { left: 25px; top: 124px; width: 160px; }
  .head-office { left: 187px; top: 124px; text-transform: none; }
  .address { left: 25px; top: 152px; width: 160px; }

  .handling-marks { position: absolute; left: 30px; top: 24px; display: flex; gap: 4px; }
  .handling-marks svg { width: 57px; height: 57px; display: block; }

  .spec-list { position: absolute; left: 30px; top: 98px; list-style: none; }
  .spec-row {
    display: flex; align-items: flex-end; height: 44px;
    font-family: "Noto Sans SC", sans-serif; font-weight: 700; font-size: 21px; color: var(--ink);
  }
  .spec-value {
    width: 120px; margin-left: 6px; margin-bottom: 6px; height: 22px;
    border-bottom: 1.5px solid var(--ink);
    font-family: "Roboto", sans-serif; font-weight: 700; font-size: 16px; line-height: 18px;
  }
</style>
</head>
<body>
<main class="canvas">
  <svg class="dieline" width="1200" height="960" viewBox="0 0 1200 960" aria-hidden="true">
    <g fill="none" stroke="var(--cut-line)" stroke-width="1.2">
      <rect x="76" y="212" width="1075" height="535"/>
      <path d="M76 334 L52 346 L52 616 L76 628"/>
    </g>
    <g fill="none" stroke="var(--fold-line)" stroke-width="1" stroke-dasharray="3 3">
      <line x1="76" y1="334" x2="1151" y2="334"/>
      <line x1="76" y1="628" x2="1151" y2="628"/>
    </g>
    <g stroke="var(--fold-line)" stroke-width="1">
      <line x1="374" y1="212" x2="374" y2="747"/>
      <line x1="614" y1="212" x2="614" y2="747"/>
      <line x1="911" y1="212" x2="911" y2="747"/>
    </g>
  </svg>

  <!-- Side A, first -->
  <section class="panel panel-side-a" style="left:76px">
    <div class="logo-slot">LOGO</div>
    <p class="slogan">we grow healthier future for you</p>
    <p class="company-name">Fujian Silverbrook Agronomic<br>Sciences Co.,Ltd</p>
    <p class="head-office">Head office Tel :<br>www.fjqlnykx.com</p>
    <p class="address">South of 317 Provincial Road,<br>East of Taoxi Township, City of Longyan,<br>Fujian Province, China</p>
  </section>

  <!-- Side B, first -->
  <section class="panel panel-side-b" style="left:374px">
    <div class="handling-marks">
      <svg viewBox="0 0 57 57" role="img" aria-label="Keep dry">
        <rect x="2" y="2" width="53" height="53" fill="none" stroke="var(--mark)" stroke-width="3"/>
        <g stroke="var(--mark)" stroke-width="1.6">
          <line x1="10" y1="9" x2="9" y2="13"/><line x1="16" y1="9" x2="15" y2="13"/><line x1="22" y1="9" x2="21" y2="13"/><line x1="28" y1="9" x2="27" y2="13"/><line x1="34" y1="9" x2="33" y2="13"/><line x1="40" y1="9" x2="39" y2="13"/><line x1="46" y1="9" x2="45" y2="13"/>
        </g>
        <path d="M10 32 Q28 10 47 32 Z" fill="var(--mark)"/>
        <path d="M28.5 30 V44 Q28.5 48 25 48 Q22 48 22 45" fill="none" stroke="var(--mark)" stroke-width="2.4"/>
      </svg>
      <svg viewBox="0 0 57 57" role="img" aria-label="This way up">
        <rect x="2" y="2" width="53" height="53" fill="none" stroke="var(--mark)" stroke-width="3"/>
        <path d="M13 22 L20 11 L27 22 H23 V40 H17 V22 Z" fill="var(--mark)"/>
        <path d="M30 22 L37 11 L44 22 H40 V40 H34 V22 Z" fill="var(--mark)"/>
        <rect x="11" y="43" width="35" height="4" fill="var(--mark)"/>
      </svg>
      <svg viewBox="0 0 57 57" role="img" aria-label="Keep away from sunlight">
        <rect x="2" y="2" width="53" height="53" fill="none" stroke="var(--mark)" stroke-width="3"/>
        <circle cx="42" cy="15" r="4" fill="var(--mark)"/>
        <g stroke="var(--mark)" stroke-width="1.5">
          <line x1="42" y1="6" x2="42" y2="9"/><line x1="42" y1="21" x2="42" y2="24"/><line x1="33" y1="15" x2="36" y2="15"/><line x1="48" y1="15" x2="51" y2="15"/>
          <line x1="36" y1="9" x2="38" y2="11"/><line x1="46" y1="19" x2="48" y2="21"/><line x1="48" y1="9" x2="46" y2="11"/><line x1="36" y1="21" x2="38" y2="19"/>
        </g>
        <path d="M7 36 L26 23 L45 36" fill="none" stroke="var(--mark)" stroke-width="3"/>
        <rect x="18" y="36" width="17" height="5" fill="var(--mark)"/>
        <rect x="14" y="43" width="25" height="5" fill="var(--mark)"/>
      </svg>
    </div>
    <ul class="spec-list">
      <li class="spec-row">品名:<span class="spec-value"></span></li>
      <li class="spec-row">规格:<span class="spec-value"></span></li>
      <li class="spec-row">重量:<span class="spec-value"></span></li>
      <li class="spec-row">体积:<span class="spec-value">65x45x56cm</span></li>
    </ul>
  </section>

  <!-- Side A, second -->
  <section class="panel panel-side-a" style="left:614px">
    <div class="logo-slot">LOGO</div>
    <p class="slogan">we grow healthier future for you</p>
    <p class="company-name">Fujian Silverbrook Agronomic<br>Sciences Co.,Ltd</p>
    <p class="head-office">Head office Tel :<br>www.fjqlnykx.com</p>
    <p class="address">South of 317 Provincial Road,<br>East of Taoxi Township, City of Longyan,<br>Fujian Province, China</p>
  </section>

  <!-- Side B, second -->
  <section class="panel panel-side-b" style="left:911px">
    <div class="handling-marks">
      <svg viewBox="0 0 57 57" role="img" aria-label="Keep dry">
        <rect x="2" y="2" width="53" height="53" fill="none" stroke="var(--mark)" stroke-width="3"/>
        <g stroke="var(--mark)" stroke-width="1.6">
          <line x1="10" y1="9" x2="9" y2="13"/><line x1="16" y1="9" x2="15" y2="13"/><line x1="22" y1="9" x2="21" y2="13"/><line x1="28" y1="9" x2="27" y2="13"/><line x1="34" y1="9" x2="33" y2="13"/><line x1="40" y1="9" x2="39" y2="13"/><line x1="46" y1="9" x2="45" y2="13"/>
        </g>
        <path d="M10 32 Q28 10 47 32 Z" fill="var(--mark)"/>
        <path d="M28.5 30 V44 Q28.5 48 25 48 Q22 48 22 45" fill="none" stroke="var(--mark)" stroke-width="2.4"/>
      </svg>
      <svg viewBox="0 0 57 57" role="img" aria-label="This way up">
        <rect x="2" y="2" width="53" height="53" fill="none" stroke="var(--mark)" stroke-width="3"/>
        <path d="M13 22 L20 11 L27 22 H23 V40 H17 V22 Z" fill="var(--mark)"/>
        <path d="M30 22 L37 11 L44 22 H40 V40 H34 V22 Z" fill="var(--mark)"/>
        <rect x="11" y="43" width="35" height="4" fill="var(--mark)"/>
      </svg>
      <svg viewBox="0 0 57 57" role="img" aria-label="Keep away from sunlight">
        <rect x="2" y="2" width="53" height="53" fill="none" stroke="var(--mark)" stroke-width="3"/>
        <circle cx="42" cy="15" r="4" fill="var(--mark)"/>
        <g stroke="var(--mark)" stroke-width="1.5">
          <line x1="42" y1="6" x2="42" y2="9"/><line x1="42" y1="21" x2="42" y2="24"/><line x1="33" y1="15" x2="36" y2="15"/><line x1="48" y1="15" x2="51" y2="15"/>
          <line x1="36" y1="9" x2="38" y2="11"/><line x1="46" y1="19" x2="48" y2="21"/><line x1="48" y1="9" x2="46" y2="11"/><line x1="36" y1="21" x2="38" y2="19"/>
        </g>
        <path d="M7 36 L26 23 L45 36" fill="none" stroke="var(--mark)" stroke-width="3"/>
        <rect x="18" y="36" width="17" height="5" fill="var(--mark)"/>
        <rect x="14" y="43" width="25" height="5" fill="var(--mark)"/>
      </svg>
    </div>
    <ul class="spec-list">
      <li class="spec-row">品名:<span class="spec-value"></span></li>
      <li class="spec-row">规格:<span class="spec-value"></span></li>
      <li class="spec-row">重量:<span class="spec-value"></span></li>
      <li class="spec-row">体积:<span class="spec-value">65x45x56cm</span></li>
    </ul>
  </section>
</main>
</body>
</html>
```